Healthcare website

We want to replace our website using joomla as the CMS. We want it to be device agnostic (gantry etc). Our business is health care our clients are people with high level spinal cord injuries ( quadriplegia / tetraplegia etc ). The site is a marketing tool primarily to potential clients and a portal for existing staff to access forms etc. It will showcase our key staff and our capability. It will also be where any new recruits apply to work with us. It must allow us to integrate our social media initiatives also. The final design must convey sophistication, high quality care and be warm and welcoming.

current web site is www.tindalehomeaid.com.au
Updates

I have made small change to the brief in that i have removed the prefered color and indicated it would be nice to see some images that symbolize change / transformation like butterflies etc. thank you

Target Market(s)

Our business is health care our clients are people with high level spinal cord injuries ( quadriplegia / tetraplegia etc ).

Industry/Entity Type

Marketing

Colors

Designer to choose colors to be used in the design.

Requirements
Must have
• The site is a marketing tool primarily to potential clients and a portal for existing staff to access forms etc. It will showcase our key staff and our capability. It will also be where any new recruits apply to work with us. It must allow us to integrate our social media initiatives also. The final design must convey sophistication, high quality care and be warm and welcoming.
Nice to have
• Would be nice to incorporate images that symbolize change and new transformations - butterflies etc.

```html
<!DOCTYPE html>
<html lang="en">
<head>
<meta charset="utf-8">
<title>Tindale Home Aid</title>
<link href="https://fonts.googleapis.com/css2?family=Open+Sans:wght@400;600&display=swap" rel="stylesheet">
<style>
:root{
  --blue:#2b6db3;
  --blue-light:#3a8ad8;
  --blue-dark:#1d5a99;
  --text:#555;
  --dark:#333;
  --grey-band:#555;
  --panel:#f2f2f2;
  --footer:#333333;
  --footer-text:#aaa;
}
*{box-sizing:border-box;margin:0;padding:0}
html,body{width:766px;height:1200px;overflow:hidden;background:#fff;font-family:'Open Sans',Arial,sans-serif;color:var(--text)}
.page{position:relative;width:766px;height:1200px}
.abs{position:absolute}

.brand{left:64px;top:28px;display:flex;align-items:center;gap:8px;font-size:22px;color:var(--blue);font-weight:600}
.brand-mark{width:30px;height:30px;border-radius:50%;background:var(--blue)}
.contact{right:88px;top:28px;text-align:right}
.contact .addr{font-size:9.5px;color:#666}
.contact .call{font-size:14px;color:#444;font-weight:600;margin-top:2px}
.contact .call span{color:var(--blue)}
.contact-icon{left:686px;top:36px}

.nav{left:0;top:92px;width:766px;height:32px;background:linear-gradient(#3c8bd6,#2565ab);border-bottom:1px solid #1d5694}
.nav ul{position:absolute;left:64px;top:0;display:flex;list-style:none;height:32px}
.nav li{height:32px;line-height:32px;font-size:10.5px;color:#fff;text-align:center;border-right:1px solid rgba(255,255,255,.25)}
.nav li.active{background:#1a4f8a}

.hero{left:63px;top:133px;width:640px;height:273px;background:#efefed}
.hero-photo{position:absolute;left:0;top:0;width:440px;height:273px;background:linear-gradient(90deg,#c9c2b8 0%,#e6e3de 45%,#efefed 100%)}
.hero-text{position:absolute;right:21px;top:70px;width:210px;text-align:right;font-size:13.5px;line-height:19px;color:var(--blue)}
.btn{position:absolute;background:#4a4a4a;color:#fff;font-size:11.5px;text-align:center;border-radius:2px;border-bottom:2px solid #2c2c2c}
.hero .btn{right:21px;top:154px;width:76px;height:26px;line-height:25px}
.arrow{position:absolute;top:200px;width:23px;height:22px;background:#666}

.welcome{left:64px;top:426px;width:472px}
.welcome h1{font-size:16px;font-weight:400;color:var(--blue);margin-bottom:9px}
.welcome p{font-size:8.3px;line-height:14.5px;margin-bottom:5px}
.welcome h2{font-size:10.5px;font-weight:600;color:#333;margin-top:6px}
.provide{left:64px;top:585px;width:472px;height:157px;background:var(--panel)}
.provide ul{position:absolute;left:11px;top:14px;width:300px;list-style:none}
.provide li{position:relative;padding-left:15px;font-size:9.2px;line-height:14.5px;margin-bottom:5.5px}
.provide li svg{position:absolute;left:0;top:4px}
.chair{position:absolute;left:328px;top:10px;width:134px;height:140px;background:radial-gradient(circle,#9a9a9a 0%,#d8d8d8 55%,var(--panel) 75%)}

.news{left:549px;top:422px;width:154px}
.news h3{height:28px;line-height:28px;padding-left:10px;font-size:13.5px;font-weight:400;color:#fff;background:linear-gradient(#3c8bd6,#2565ab)}
.news-item{position:relative;height:55px;margin-top:3px;background:var(--panel)}
.news-item .thumb{position:absolute;left:6px;top:7px;width:48px;height:40px}
.news-item .title{position:absolute;left:61px;top:5px;font-size:8.3px;line-height:11px;color:#333}
.news-item .date{position:absolute;left:61px;top:33px;font-size:7.5px;color:#777}

.values{left:63px;top:764px;width:640px;height:54px;background:var(--grey-band)}
.value{position:absolute;top:10px;display:flex;align-items:center;font-size:16px;color:#fff}
.value b{width:34px;height:34px;border-radius:50%;background:#fff;color:var(--blue);font-weight:400;font-size:19px;text-align:center;line-height:34px;margin-right:3px}

.join{left:0;top:838px;width:766px;text-align:center}
.join h2{font-size:15px;font-weight:400;color:var(--blue)}
.join p{font-size:9.7px;color:#444;margin-top:4px}
.join .btn{position:relative;display:inline-block;margin-top:8px;width:76px;height:26px;line-height:25px}

.rule{left:64px;width:640px;height:1px;background:#e3e3e3}
.partners{left:0;top:956px;width:766px;display:flex;justify-content:center;align-items:center;gap:22px}
.partners span{display:block;background:#d5d5d5}

.footer{left:0;top:1013px;width:766px;height:187px;background:var(--footer)}
.foot-links{position:absolute;left:0;top:18px;width:766px;display:flex;justify-content:center;gap:38px;list-style:none;font-size:8.3px;color:var(--footer-text)}
.foot-links li::before{content:"• ";color:#888}
.foot-rule{position:absolute;left:64px;width:640px;height:1px;background:#484848}
.foot-about{position:absolute;left:80px;top:62px;width:606px;text-align:center;font-size:7.5px;line-height:13.5px;color:#8a8a8a}
.copy{position:absolute;left:64px;top:149px;font-size:8.3px;color:#bbb}
.social{position:absolute;top:145px;width:21px;height:21px;border-radius:50%;border:2px solid #222}
</style>
</head>
<body>
<div class="page">

  <header>
    <div class="abs brand"><span class="brand-mark"></span>Tindale Home Aid</div>
    <div class="abs contact">
      <div class="addr">42 - 44 Harbour View Rd, Glenwood, Victoria, 3041</div>
      <div class="call">Call us : <span>(03) 9000 4127</span></div>
    </div>
    <svg class="abs contact-icon" width="17" height="20" viewBox="0 0 17 20"><rect x="2" y="1" width="13" height="18" rx="1.5" fill="#444"/><rect x="4" y="3" width="9" height="14" fill="#fff"/><text x="8.5" y="13" font-size="8" text-anchor="middle" fill="#444" font-family="Open Sans,sans-serif">@</text></svg>
  </header>

  <nav class="abs nav">
    <ul>
      <li class="active" style="width:77px">HOME</li>
      <li style="width:102px">ABOUT US</li>
      <li style="width:120px">OUR SERVICES</li>
      <li style="width:110px">RESOURCES</li>
      <li style="width:114px">CONTACT US</li>
      <li style="width:116px">TESTIMONIALS</li>
    </ul>
  </nav>

  <section class="abs hero">
    <div class="hero-photo" role="img" aria-label="Doctor reviewing a spinal x-ray with a patient in a bright clinic"></div>
    <p class="hero-text">Tindale Home Aid is a small team of care professionals committed to providing quality one-to-one care with heart.</p>
    <div class="btn">Contact Us</div>
    <div class="arrow" style="left:570px"><svg width="23" height="22"><path d="M16 11H7M11 7l-4 4 4 4" stroke="#fff" stroke-width="2" fill="none"/></svg></div>
    <div class="arrow" style="left:595px"><svg width="23" height="22"><path d="M7 11h9M12 7l4 4-4 4" stroke="#fff" stroke-width="2" fill="none"/></svg></div>
  </section>

  <section class="abs welcome">
    <h1>Welcome to Tindale Home Aid</h1>
    <p>Tindale Home Aid has built its service around the needs of each and every client. We listen to and consult with our clients, their families, Care Teams and the wider care community. Tindale Home Aid is a privately owned organisation providing in home care for people with disabilities (attendant care) throughout the State of Victoria. We commenced operation on the 1st of July 2004 at our principal office in Glenwood, Victoria.</p>
    <p>We are committed to our Vision - "to provide the BEST care" and we are fully accountable to our clients, carers and funding organisations. We are solely focused on providing the best care and we continuously innovate to ensure we do this.</p>
    <h2>At Tindale Home Aid we provide :</h2>
  </section>

  <section class="abs provide">
    <ul>
      <li><svg width="9" height="7"><path d="M1 3.5l2.5 2.5L8 1" stroke="#666" stroke-width="1.3" fill="none"/></svg>Professionally supported one-to-one home based care</li>
      <li><svg width="9" height="7"><path d="M1 3.5l2.5 2.5L8 1" stroke="#666" stroke-width="1.3" fill="none"/></svg>Expert specialist care for clients with SCI &amp; ABI</li>
      <li><svg width="9" height="7"><path d="M1 3.5l2.5 2.5L8 1" stroke="#666" stroke-width="1.3" fill="none"/></svg>Assistance with daily living tasks community and recreation access</li>
      <li><svg width="9" height="7"><path d="M1 3.5l2.5 2.5L8 1" stroke="#666" stroke-width="1.3" fill="none"/></svg>Tindale Home Aid is available 24 hours seven days per week.</li>
      <li><svg width="9" height="7"><path d="M1 3.5l2.5 2.5L8 1" stroke="#666" stroke-width="1.3" fill="none"/></svg>Tindale Home Aid is Road Injury Authority (RIA), State Workplace Care Authority (SWCA) and Department of Community Support (DCS) approved.</li>
    </ul>
    <div class="chair" role="img" aria-label="Wheelchair"></div>
  </section>

  <aside class="abs news">
    <h3>Latest News</h3>
    <div class="news-item"><div class="thumb" role="img" aria-label="Group celebrating with blue balloons" style="background:linear-gradient(#3a4f9a,#6a4a6a)"></div><div class="title">Phasellus elementum dignissim molestie</div><div class="date">June 18, 2014</div></div>
    <div class="news-item"><div class="thumb" role="img" aria-label="Client outdoors on a sunny lawn" style="background:linear-gradient(#8fb7d8,#7a9a5a)"></div><div class="title">Phasellus elementum dignissim molestie</div><div class="date">June 18, 2014</div></div>
    <div class="news-item"><div class="thumb" role="img" aria-label="Smiling client portrait" style="background:linear-gradient(#c9a98a,#8a6a5a)"></div><div class="title">Phasellus elementum dignissim molestie</div><div class="date">June 18, 2014</div></div>
    <div class="news-item"><div class="thumb" role="img" aria-label="Silhouette at sunset" style="background:linear-gradient(#e0902a,#3a2a1a)"></div><div class="title">Phasellus elementum dignissim molestie</div><div class="date">June 18, 2014</div></div>
    <div class="news-item"><div class="thumb" role="img" aria-label="Carer walking with a client" style="background:linear-gradient(#6a8a6a,#3a4a5a)"></div><div class="title">Phasellus elementum dignissim molestie</div><div class="date">June 18, 2014</div></div>
  </aside>

  <section class="abs values">
    <div class="value" style="left:27px"><b>C</b>ommittment</div>
    <div class="value" style="left:194px"><b>A</b>chievement</div>
    <div class="value" style="left:355px"><b>R</b>espect</div>
    <div class="value" style="left:481px"><b>E</b>mpowerment</div>
  </section>

  <section class="abs join">
    <h2>Join Our Team</h2>
    <p>We are always on the lookout for great people to work with our clients. If you want to be a part of our Team click below to apply.</p>
    <div class="btn">Apply Now</div>
  </section>

  <div class="abs rule" style="top:934px"></div>
  <div class="abs partners">
    <span style="width:18px;height:24px"></span>
    <span style="width:36px;height:16px"></span>
    <span style="width:28px;height:14px"></span>
    <span style="width:44px;height:32px;border-radius:50% 50% 4px 4px"></span>
    <span style="width:64px;height:20px"></span>
    <span style="width:18px;height:20px"></span>
    <span style="width:20px;height:30px"></span>
  </div>

  <footer class="abs footer">
    <ul class="foot-links">
      <li>Home</li><li>About us</li><li>Our Services</li><li>Resources</li><li>Contact us</li><li>Testimonials</li>
    </ul>
    <div class="foot-rule" style="top:45px"></div>
    <p class="foot-about">Tindale Home Aid is proud to be an approved provider for Road Injury Authority (RIA), State Workplace Care Authority (SWCA), Department of Community Support (DCS) and maintain associations and cooperative relationships with a variety of private and governmental organisations in its efforts to bring the finest, most up-to-date care for its clients.</p>
    <div class="foot-rule" style="top:125px"></div>
    <p class="copy">Copyright &copy; 2014 Tindale Home Aid Pty Ltd.&nbsp; All rights reserved.&nbsp; |&nbsp; Privacy &nbsp;|&nbsp; Terms of Service</p>
    <span class="social" style="left:593px;background:#2f5a9e"></span>
    <span class="social" style="left:622px;background:#3aa6e0"></span>
    <span class="social" style="left:651px;background:#1f7ab8"></span>
    <span class="social" style="left:680px;background:#f07a22"></span>
  </footer>

</div>
</body>
</html>
```